Dorsey K. Wendell Business Card

We need a business card for our company Dorsey K. Wendell Heating & Plumbing to be distributed to potential customers. It should follow the color scheme of our logo and have a modern upscale and masculine look.

The logo is attached and the info below should also be included:

5187 W. Cedar Brook Rd.
Manheim, PA 17545

Russell T. Wendell
(717) 592-0817
russelltwendell@fernmail.net
dorseykwendell.net
PA #093148

Industry/Entity Type

Business

Contact Information for Business Card

5187 W. Cedar Brook Rd.
Manheim, PA 17545

Russell T. Wendell
(717) 592-0817
russelltwendell@fernmail.net
dorseykwendell.net
PA #093148

Colors

Designer to choose colors to be used in the design.

Requirements
Must have
• Information above included

```html
<!DOCTYPE html>
<html lang="en">
<head>
<meta charset="utf-8">
<title>Dorsey K. Wendell Business Card</title>
<link rel="stylesheet" href="https://fonts.googleapis.com/css2?family=Jost:wght@400;500;600;700&display=swap">
<style>
  :root {
    --backdrop: #eeeae3;
    --card-white: #ffffff;
    --brand-blue: #0b4f9e;
    --brand-green: #a8d444;
    --green-deep: #93c236;
    --ink: #3d3d3d;
    --ink-soft: #5a5a5a;
    --steel: #b9bec4;
    --skin-tone: #e9b48a;
    --overall-blue: #6f8fb3;
  }
  * { box-sizing: border-box; margin: 0; padding: 0; }
  html, body {
    width: 1200px; height: 800px; overflow: hidden;
    background: var(--backdrop);
    font-family: "Jost", "Futura", sans-serif;
  }
  .canvas {
    position: relative; width: 1200px; height: 800px;
    display: flex; align-items: center; justify-content: center; gap: 50px;
  }
  .card {
    position: relative; width: 525px; height: 300px; overflow: hidden;
    box-shadow: 0 6px 18px rgba(0,0,0,.18);
  }
  /* front */
  .card--front { background: var(--card-white); }
  .plumber-art {
    position: absolute; left: 22px; top: 100px; width: 160px; height: 195px;
    border-radius: 60px 60px 10px 10px;
    background: linear-gradient(180deg, var(--steel) 0%, var(--skin-tone) 30%, #e88a3a 48%, var(--overall-blue) 70%, #8a8a8a 100%);
    opacity: .85;
  }
  .faucet-art {
    position: absolute; right: 30px; top: 0; width: 95px; height: 100px;
    border-radius: 0 0 40px 40px;
    background: linear-gradient(180deg, #d7dbe0 0%, #9aa2ab 60%, #c9ced4 100%);
  }
  .brand {
    position: absolute; left: 198px; top: 118px;
    display: flex; align-items: center; gap: 10px;
    color: var(--brand-blue); font-weight: 600;
  }
  .brand__mark { width: 46px; height: 46px; background: var(--brand-blue); }
  .brand__name { font-size: 22px; line-height: 1.05; letter-spacing: .5px; text-transform: uppercase; }
  .brand__name small { display: block; font-size: 12px; letter-spacing: 1.2px; }
  .band {
    position: absolute; left: 190px; right: 0; top: 178px; height: 30px;
    background: var(--brand-blue);
    display: flex; align-items: center; padding-left: 12px;
  }
  .band__web { color: var(--card-white); font-weight: 700; font-size: 17px; letter-spacing: .3px; }
  .contact-person {
    position: absolute; left: 212px; top: 228px;
    color: var(--ink); font-size: 16px; line-height: 1.6;
  }
  .contact-person .phone { color: var(--ink-soft); letter-spacing: .5px; }
  /* back */
  .card--back { background: var(--brand-green); }
  .pipe-pattern {
    position: absolute; inset: 0;
    background: linear-gradient(135deg, var(--brand-green) 0%, var(--green-deep) 50%, var(--brand-green) 100%);
  }
  .band--back {
    position: absolute; left: 90px; right: 0; top: 168px; height: 80px;
    background: var(--brand-blue);
    display: flex; align-items: center; padding-left: 84px;
  }
  .back-mark {
    position: absolute; left: 98px; top: 162px; width: 66px; height: 66px;
    background: var(--brand-blue); border: 3px solid var(--brand-green);
  }
  .address { color: var(--card-white); font-size: 14.5px; line-height: 1.25; letter-spacing: .3px; }
</style>
</head>
<body>
<main class="canvas">
  <section class="card card--front" aria-label="Business card front">
    <div class="plumber-art" role="img" aria-label="Cartoon plumber carrying a pipe and wrench"></div>
    <div class="faucet-art" role="img" aria-label="Chrome faucet with a falling water drop"></div>
    <div class="brand">
      <span class="brand__mark"></span>
      <p class="brand__name">Dorsey K. Wendell<small>Heating &amp; Plumbing</small></p>
    </div>
    <div class="band"><span class="band__web">dorseykwendell.net</span></div>
    <div class="contact-person">
      <p class="name">Russell T. Wendell</p>
      <p class="phone">(717) 592-0817</p>
    </div>
  </section>

  <section class="card card--back" aria-label="Business card back">
    <div class="pipe-pattern" role="img" aria-label="Faint pattern of connected plumbing pipes"></div>
    <div class="band--back">
      <p class="address">5187 W. Cedar Brook Rd.<br>Manheim, PA 17545<br>russelltwendell@fernmail.net<br>PA #093148</p>
    </div>
    <span class="back-mark"></span>
  </section>
</main>
</body>
</html>
```